Pitch Mentors UK award course Flyer Design

Flyer design required for a social enterprise called "Backing Play" - logo attached - to promote our Pitch Mentors Award course(s).

The course is targeted at individuals aged 13+ and will develop leadership skills that transfer beyond the sporting environment. It is a fun and practical course that focusses on leading rather than sporting ability or technical knowledge and leads on to further qualifications or awards. Individuals' self-confidence will improve and the course is a potential stepping stone in to employment, further education or training.

The course will be run at Brambleford Community Sports Centre, Oxhurst School, Tolbery Lane, Ashcombe. QT4 7RW. On Monday 20th July to Friday 24th July.
There is a subsidised fee of £15

We are a Regional Academy for Pitch Mentors UK.

The company's main colour is royal blue but please make the design as attractive and eye-catching to young people, male and female, as possible.

```html
<!DOCTYPE html>
<html lang="en">
<head>
<meta charset="utf-8">
<title>Pitch Mentors Award Course Flyer</title>
<link rel="stylesheet" href="https://fonts.googleapis.com/css2?family=Arimo:wght@400;700&display=swap">
<style>
  :root {
    --backdrop: #9ba097;
    --royal: #1746a2;
    --navy: #171d2b;
    --sky: #4fb4ea;
    --white: #ffffff;
    --band-text: #e4ecf8;
    --photo-sky: #a9c6de;
    --photo-warm: #e7b23c;
    --photo-ground: #b07a2c;
  }
  html, body {
    margin: 0;
    width: 1200px;
    height: 900px;
    overflow: hidden;
    background: var(--backdrop);
  }
  .stage {
    position: relative;
    width: 1200px;
    height: 900px;
  }
  .flyer {
    position: absolute;
    left: 50px;
    top: 60px;
    width: 1100px;
    height: 780px;
    display: block;
  }
  .flyer text {
    font-family: "Arimo", Arial, sans-serif;
  }
  .band-title { fill: var(--band-text); font-weight: 700; font-size: 34px; }
  .venue-name { fill: var(--white); font-weight: 700; font-size: 21px; }
  .venue-address { fill: var(--white); font-weight: 400; font-size: 20px; }
  .dates { fill: var(--white); font-weight: 700; font-size: 25px; }
  .dates .day { fill: var(--sky); font-weight: 400; }
  .dates .joiner { font-size: 17px; font-weight: 400; }
  .find-out { fill: var(--white); font-weight: 400; font-size: 21px; }
  .web-address { fill: var(--white); font-weight: 700; font-size: 25px; }
  .brand-name { fill: var(--royal); font-weight: 700; font-size: 27px; }
</style>
</head>
<body>
<main class="stage">
  <svg class="flyer" viewBox="0 0 886 628" xmlns="http://www.w3.org/2000/svg" aria-label="Pitch Mentors Award Course flyer">
    <defs>
      <linearGradient id="photoTone" x1="0" y1="0" x2="0.3" y2="1">
        <stop offset="0" stop-color="var(--photo-sky)"/>
        <stop offset="0.45" stop-color="#c9c6a8"/>
        <stop offset="0.7" stop-color="var(--photo-warm)"/>
        <stop offset="1" stop-color="var(--photo-ground)"/>
      </linearGradient>
    </defs>

    <rect class="hero-photo" x="0" y="0" width="886" height="460" fill="url(#photoTone)"
          role="img" aria-label="Photo of a girls' team in yellow kit standing arm in arm, seen from behind, under a blue sky"/>

    <polygon class="accent-corner" points="686,0 783,0 886,88 886,168" fill="var(--royal)"/>
    <polygon class="accent-side" points="0,145 205,345 300,628 0,628" fill="var(--royal)"/>

    <polygon class="info-panel" points="265,440 886,212 886,628 285,628" fill="var(--navy)"/>

    <polygon class="headline-band" points="263,360 886,147 886,235 278,448" fill="var(--royal)"/>
    <text class="band-title" transform="translate(303,414) rotate(-20)">PITCH MENTORS AWARD COURSE</text>

    <polygon class="logo-card" points="0,418 262,338 313,515 48,595 0,595" fill="var(--white)"/>
    <polygon class="logo-card-tab" points="48,585 300,508 312,545 60,622" fill="var(--white)"/>
    <line class="speed-line" x1="40" y1="372" x2="150" y2="332" stroke="var(--white)" stroke-width="4"/>
    <line class="speed-line" x1="58" y1="388" x2="140" y2="358" stroke="var(--white)" stroke-width="4"/>
    <circle class="brand-dot" cx="40" cy="474" r="9" fill="var(--sky)"/>
    <text class="brand-name" x="58" y="484">Backing Play</text>

    <text class="venue-name" transform="translate(356,478) rotate(-20)">BRAMBLEFORD COMMUNITY SPORTS CENTRE</text>
    <text class="venue-address" transform="translate(418,488) rotate(-20)">TOLBERY LANE, ASHCOMBE. QT4 7RW</text>
    <text class="dates" transform="translate(381,555) rotate(-20)"><tspan class="day">MONDAY</tspan>20TH JULY <tspan class="joiner">TO</tspan> <tspan class="day">FRIDAY</tspan>24TH JULY</text>
    <text class="find-out" transform="translate(613,525) rotate(-20)">Find out more at</text>

    <polygon class="web-strip" points="543,558 886,443 886,503 560,612" fill="var(--royal)"/>
    <text class="web-address" transform="translate(575,589) rotate(-20)">www.backingplay.org</text>
  </svg>
</main>
</body>
</html>
```